Vornel Technologies business card design

We need a business card designed with our new logo. it would be great if the card could communicate it is a technology based company.

Target Market(s)

system integrators

Industry/Entity Type

technology, IOT

Contact Information for Business Card

Name, designation, Address, telephone number, email address

Requirements
Must have
• logo and company name
Nice to have
• something to do with technology

```html
<!DOCTYPE html>
<html lang="en">
<head>
<meta charset="utf-8">
<title>Vornel Technologies — Business Card</title>
<link href="https://fonts.googleapis.com/css2?family=Open+Sans:wght@400;600;700;800&display=swap" rel="stylesheet">
<style>
  :root {
    --backdrop: #3b3b3b;
    --card: #1a1a1a;
    --card-back: #161616;
    --accent: #f39a1e;
    --text: #e8e8e8;
    --muted: #2c2c2c;
  }
  * { box-sizing: border-box; margin: 0; padding: 0; }
  html, body { width: 1200px; height: 801px; overflow: hidden; }
  body {
    background: var(--backdrop);
    font-family: "Open Sans", Arial, sans-serif;
    position: relative;
  }
  .card {
    position: absolute;
    top: 252px;
    width: 525px;
    height: 300px;
    background: var(--card);
    border-left: 3px solid var(--accent);
    border-bottom: 3px solid var(--accent);
  }
  .card--front { left: 58px; }
  .card--back { left: 617px; background: var(--card-back); }

  .brand {
    position: absolute;
    top: 34px;
    right: 38px;
    display: flex;
    align-items: center;
    gap: 10px;
  }
  .brand__mark { width: 16px; height: 16px; background: var(--accent); }
  .brand__name {
    color: #ffffff;
    font-weight: 800;
    font-size: 22px;
    letter-spacing: 1px;
    text-transform: uppercase;
  }

  .person { position: absolute; left: 38px; top: 134px; }
  .person__name {
    color: var(--accent);
    font-weight: 700;
    font-size: 21px;
    text-transform: uppercase;
    line-height: 1.1;
  }
  .person__role { color: var(--text); font-size: 14px; margin-top: 2px; }

  .divider {
    position: absolute;
    left: 38px;
    right: 38px;
    top: 196px;
    height: 1px;
    background: var(--accent);
  }

  .contacts { position: absolute; left: 38px; top: 210px; list-style: none; }
  .contacts li {
    display: flex;
    align-items: center;
    gap: 9px;
    color: var(--text);
    font-size: 13.5px;
    line-height: 22px;
  }
  .contacts svg { width: 11px; height: 11px; flex: none; }

  .address {
    position: absolute;
    right: 38px;
    top: 210px;
    text-align: right;
    color: var(--text);
    font-size: 13.5px;
    line-height: 20px;
  }

  .back-brand {
    position: absolute;
    inset: 0;
    display: flex;
    align-items: center;
    justify-content: center;
    gap: 12px;
  }
  .back-brand__mark { width: 22px; height: 22px; background: var(--muted); }
  .back-brand__name {
    color: var(--muted);
    font-weight: 800;
    font-size: 30px;
    letter-spacing: 1px;
    text-transform: uppercase;
  }
</style>
</head>
<body>
  <section class="card card--front" aria-label="Business card front">
    <div class="brand">
      <span class="brand__mark"></span>
      <span class="brand__name">Vornel Technologies</span>
    </div>

    <div class="person">
      <p class="person__name">Dario Kessling</p>
      <p class="person__role">President</p>
    </div>

    <div class="divider"></div>

    <ul class="contacts">
      <li>
        <svg viewBox="0 0 12 12" aria-hidden="true"><path fill="#f39a1e" d="M2.4 0.8l2 2-1 1.4c.6 1.4 1.6 2.4 3 3l1.4-1 2 2-1.2 1.8C5 10 2 7 .6 2z"/></svg>
        555-310-4827
      </li>
      <li>
        <svg viewBox="0 0 12 12" aria-hidden="true"><rect x="0.5" y="2" width="11" height="8" fill="#f39a1e"/><path d="M0.5 2l5.5 4.5L11.5 2" fill="none" stroke="#1a1a1a" stroke-width="1.2"/></svg>
        info@vorneltechnologies.com
      </li>
      <li>
        <svg viewBox="0 0 12 12" aria-hidden="true"><circle cx="6" cy="6" r="5" fill="none" stroke="#f39a1e" stroke-width="1.4"/><path d="M1 6h10M6 1c-2.5 3-2.5 7 0 10M6 1c2.5 3 2.5 7 0 10" fill="none" stroke="#f39a1e" stroke-width="1"/></svg>
        www.vorneltechnologies.com
      </li>
    </ul>

    <p class="address">1870 Marlow Bay Drive<br>Cedar Point CA 90417</p>
  </section>

  <section class="card card--back" aria-label="Business card back">
    <div class="back-brand">
      <span class="back-brand__mark"></span>
      <span class="back-brand__name">Vornel</span>
    </div>
  </section>
</body>
</html>
```